Geschäftspapier-Design für Anbieter einer Online-Ausbildung für den qualifizierten Krankentransport und Rettungsdienst
Zielgruppe
LOTH Online-Ausbildung für den qualifizierten Krankentransport und Rettungsdienst
Der qualifizierte Krankentransport und Rettungsdienst ist zuständig für den Transport- und die Versorgung von kranken und verletzten Menschen. LOTH Medizinische Ausbildung und Seminare hat sich als Privatschule für die präklinische Notfallmedizin auf Aus- und Weiterbildungen im E-Learning-Modul für diese zwei Fachbereiche spezialisiert. Alle unsere Fachausbildungen sind online in unserem modernen Campus mit überregionalem Zugang absolvierbar.
Aufgabenstellung
Wir benötigen eine Word-Briefvorlage für den alltäglichen Geschäftsverkehr in drei Ausführungen.
- Briefvorlage mit Angabe der Abteilung -> Sekretariat
- Briefvorlage mit Angabe der Abteilung -> Schulleitung
- Briefvorlage mit Angabe der Abteilung -> Geschäftsführung
- Briefvorlage mit Angabe der Abteilung -> Buchhaltung/ Forderungsmanagement
Die Vorlage sollte bitte folgende Angaben aufweisen:
LOTH Bildungsgesellschaft UG (haftungsbeschränkt)
Privatschule für prähospitale Rettungsmedizin
Standort unserer Verwaltung:
Farnhügel 7
15537 Erkner
Standort unseres Schulsitzes:
Am Quendelhof 48
D- 15537 Gosen- Neu Zittau
Schulleitung: Jutta Wildgrube & Matthias Lot
Ärztliche Leitung: Dr. Med. Ortwin Brasch
Pädagogische Leitung: Matthias Loth
Fachlicher Beirat: Dr. rer. med. Fabian Oswalt
Tel: 030 6270384 50
Fax: 030 6270384 51
E-Mail: info@loth-lehrwerkstatt.de
Web: www.loth-lehrwerkstatt.de
Vertreten durch: Jutta Wildgrube
Registereintrag: Eintragung im Handelsregister Registergericht: Amtsgericht Frankfurt (Oder) Registernummer: HRB 27403 FF

```html
<!DOCTYPE html>
<html lang="de">
<head>
<meta charset="utf-8">
<title>LOTH Briefvorlage – Schulleitung</title>
<link href="https://fonts.googleapis.com/css2?family=Tinos:wght@400;700&family=Open+Sans:wght@400;600;700&display=swap" rel="stylesheet">
<style>
  :root {
    --brand-blue: #6ea6d6;
    --ink: #1a1a1a;
    --rule: #222;
    --paper: #ffffff;
  }
  * { margin: 0; padding: 0; box-sizing: border-box; }
  html, body { width: 862px; height: 1200px; overflow: hidden; background: var(--paper); }
  .letter { position: relative; width: 862px; height: 1200px; color: var(--ink); font-family: "Tinos", "Times New Roman", serif; }
  .abs { position: absolute; }

  .frame { left: 37px; top: 43px; width: 786px; height: 1111px; border: 1px solid var(--rule); }
  .band { left: 37px; width: 786px; height: 15px; background: var(--brand-blue); }
  .band--top { top: 58px; }
  .band--bottom { top: 1125px; }
  .hline { left: 37px; width: 786px; height: 1px; background: var(--rule); }
  .hline--top { top: 78px; }
  .hline--bottom { top: 1119px; }
  .fold-mark { left: 37px; width: 15px; height: 1px; background: var(--rule); }

  .brand-mark { left: 498px; top: 143px; width: 82px; display: flex; align-items: center; gap: 6px;
    font-family: "Open Sans", Arial, sans-serif; font-weight: 700; font-size: 22px; line-height: 1; color: var(--brand-blue); }
  .brand-mark .square { width: 11px; height: 11px; background: var(--brand-blue); flex: none; }

  .sidebar-rule { left: 590px; top: 104px; width: 1px; height: 301px; background: var(--brand-blue); }

  .sidebar { left: 598px; top: 127px; width: 220px; font-family: "Open Sans", Arial, sans-serif; }
  .company-name { font-weight: 600; font-size: 12px; line-height: 16px; color: #2a2a2a; }
  .company-claim { font-weight: 600; font-size: 12px; line-height: 16px; color: #2a2a2a; margin-top: 3px; }
  .department { font-weight: 700; font-size: 13px; color: var(--brand-blue); margin-top: 30px; }
  .contact { font-size: 10.4px; line-height: 14px; color: #2a2a2a; }
  .contact .label { color: var(--brand-blue); }
  .contact .block { margin-top: 4px; }
  .contact .block.first { margin-top: 8px; }

  .sender-line { left: 139px; top: 221px; font-family: "Open Sans", Arial, sans-serif; font-size: 8.6px;
    border-bottom: 1px solid var(--rule); padding-bottom: 1px; width: 262px; white-space: nowrap; }
  .recipient { left: 155px; top: 251px; font-size: 15.9px; line-height: 19px; }
  .recipient p + p { margin-top: 19px; }

  .subject { left: 113px; top: 458px; font-weight: 700; font-size: 18.5px; line-height: 22px; white-space: nowrap; }

  .body-text { left: 113px; top: 563px; width: 680px; font-size: 15.8px; line-height: 19px; }
  .body-text p + p { margin-top: 19px; }
  .body-text .line { display: block; white-space: nowrap; }

  .signature { left: 139px; top: 955px; width: 112px; height: 64px; background: linear-gradient(135deg, #f1f1f1, #dcdcdc); border-radius: 4px; }

  .footer-col { top: 1062px; padding-left: 8px; border-left: 1px solid var(--brand-blue);
    font-family: "Open Sans", Arial, sans-serif; font-size: 8.4px; line-height: 12px; white-space: nowrap; }
  .footer-col .label { color: var(--brand-blue); font-weight: 600; }
  .footer-col--team { left: 83px; }
  .footer-col--legal { left: 340px; }
  .footer-col--bank { left: 590px; }
</style>
</head>
<body>
<div class="letter">
  <div class="abs frame"></div>
  <div class="abs band band--top"></div>
  <div class="abs hline hline--top"></div>
  <div class="abs hline hline--bottom"></div>
  <div class="abs band band--bottom"></div>
  <div class="abs fold-mark" style="top:435px"></div>
  <div class="abs fold-mark" style="top:599px"></div>

  <div class="abs brand-mark"><span class="square"></span>LOTH</div>
  <div class="abs sidebar-rule"></div>

  <div class="abs sidebar">
    <p class="company-name">LOTH Bildungsgesellschaft UG<br>(haftungsbeschränkt)</p>
    <p class="company-claim">Privatschule für<br>prähospitale Rettungsmedizin</p>
    <p class="department">– Schulleitung –</p>
    <div class="contact">
      <div class="block first"><span class="label">Verwaltung:</span><br>Farnhügel 7<br>15537 Erkner</div>
      <div class="block"><span class="label">Schulsitz:</span><br>Am Quendelhof 48<br>15537 Gosen-Neu Zittau</div>
      <div class="block">Tel. 030&nbsp; 6270384 50<br>Fax 030&nbsp; 6270384 51</div>
      <div class="block">E-Mail: info@loth-lehrwerkstatt.de<br>Web: www.loth-lehrwerkstatt.de</div>
    </div>
  </div>

  <div class="abs sender-line">LOTH Bildungsgesellschaft UG&nbsp; |&nbsp; Farnhügel 7&nbsp; |&nbsp; 15537 Erkner</div>

  <div class="abs recipient">
    <p>Firma Mustermann<br>(z. Hd. Herrn Heinz Muster)</p>
    <p>Beispielstraße 48</p>
    <p>D-98765 Musterstadt</p>
  </div>

  <h1 class="abs subject">Bestätigung Ihres Termins in unserer Privatschule<br>für den Kurs „Einführung in die prähospitale Rettungsmedizin“<br>vom 7. 11. 2022 – 18. 11. 2022</h1>

  <div class="abs body-text">
    <p>
      <span class="line">Sehr geehrter Herr Heinz Muster,</span>
      <span class="line">hiermit bestätigen wir Ihnen den oben genannten Termin und so weiter, und so weiter. Dies ist ein soge-</span>
      <span class="line">nannter Blindtext, den man für Entwurfszwecke einsetz. hiermit bestätigen wir Ihnen den oben genann-</span>
      <span class="line">ten Termin und so weiter, und so weiter. Dies ist ein sogenannter Blindtext, den man für</span>
      <span class="line">Entwurfszwecke einsetz. hiermit bestätigen wir Ihnen den oben genannten Termin und so weiter, und so</span>
      <span class="line">weiter. Dies ist ein sogenannter Blindtext, den man für Entwurfszwecke einsetz.</span>
    </p>
    <p>
      <span class="line">hiermit bestätigen wir Ihnen den oben genannten Termin und so weiter, und so weiter. Dies ist ein soge-</span>
      <span class="line">nannter Blindtext, den man für Entwurfszwecke einsetz. hiermit bestätigen wir Ihnen den oben genann-</span>
      <span class="line">ten Termin und so weiter, und so weiter. Dies ist ein sogenannter Blindtext, den man für</span>
      <span class="line">Entwurfszwecke einsetz. hiermit bestätigen wir Ihnen den oben genannten Termin und so weiter, und so</span>
      <span class="line">weiter. Dies ist ein sogenannter Blindtext, den man für Entwurfszwecke einsetz.</span>
    </p>
    <p>
      <span class="line">hiermit bestätigen wir Ihnen den oben genannten Termin und so weiter, und so weiter. Dies ist ein soge-</span>
      <span class="line">nannter Blindtext, den man für Entwurfszwecke einsetz. hiermit bestätigen wir Ihnen den oben genann-</span>
      <span class="line">ten Termin und so weiter, und so weiter. Dies ist ein sogenannter Blindtext, den man für</span>
      <span class="line">Entwurfszwecke einsetz.</span>
    </p>
    <p>
      <span class="line">Mit freundlichen Grüßen,</span>
      <span class="line">Jutta Wildgrube</span>
    </p>
  </div>

  <div class="abs signature" role="img" aria-label="Handschriftliche Unterschrift"></div>

  <div class="abs footer-col footer-col--team">
    <span class="label">Schulleitung:</span> Jutta Wildgrube · Matthias Loth<br>
    <span class="label">Ärztliche Leitung:</span> Dr. med. Ortwin Brasch<br>
    <span class="label">Pädagogische Leitung:</span> Matthias Loth<br>
    <span class="label">Fachlicher Beirat:</span> Dr. rer. med. Fabian Oswalt
  </div>
  <div class="abs footer-col footer-col--legal">
    <span class="label">Vertreten durch:</span> Jutta Wildgrube<br>
    <span class="label">Registereintrag:</span> Eintragung im Handelsregister<br>
    <span class="label">Registergericht:</span> Amtsgericht Frankfurt (Oder)<br>
    <span class="label">Registernummer:</span> HRB 27403 FF
  </div>
  <div class="abs footer-col footer-col--bank">
    <span class="label">Kontoverbindung:</span><br>
    Märkische Kreditbank<br>
    IBAN: DE00 0000 0000 0000 0000 00<br>
    BIC: XXXXXXXXXXX
  </div>
</div>
</body>
</html>
```